Banner Ad Design Project

I need a nice banner ad for my company. I do IT development and IT Consulting. The banner should contain my company Logo (see my website www.bramtor-lune.net) and should use the colors from my website (www.bramtor-lune.net). The final design should communicate trust, creativity and competence. It would by nice, when the banner has some animation effects.

Target Market(s)

Manager, IT Directors, IT Decider, HR Manager, Business People

Industry/Entity Type

It Company

Requirements
Must have
• Use my company logo
Use my colors from my website
Technology oriented
Serious but not boring
Some animation
Should not have
• Sound

```html
<!DOCTYPE html>
<html lang="en">
<head>
<meta charset="utf-8">
<title>Bramtor Lune – Banner Frames</title>
<link rel="stylesheet" href="https://fonts.googleapis.com/css2?family=Arimo:wght@400;700&display=swap">
<style>
  :root {
    --page-bg: #ffffff;
    --frame-line: #1a1a1a;
    --yellow-light: #fff3a8;
    --yellow: #f9d423;
    --yellow-deep: #f2b705;
    --panel-rim: #9a9a9a;
    --panel-shadow: #5e5e5e;
    --text-dark: #111111;
    --text-grey: #6b6b6b;
    --accent-red: #e01b0f;
    --button-top: #ffd257;
    --button-bottom: #f08a00;
    --button-rim: #3b3024;
    --brand: #e3a400;
    --photo-dark: #2c3140;
    --photo-mid: #6f7a94;
    --photo-light: #d9c2a8;
  }
  * { box-sizing: border-box; margin: 0; padding: 0; }
  html, body {
    width: 857px; height: 1200px; overflow: hidden;
    background: var(--page-bg);
    font-family: "Arimo", Arial, sans-serif;
  }
  .sheet { position: relative; width: 857px; height: 1200px; }

  .banner {
    position: absolute; left: 140px; width: 521px; height: 436px;
    border: 2px solid var(--frame-line); overflow: hidden; background: #fff;
  }
  .banner--a { top: 66px; }
  .banner--b { top: 656px; }
  .banner__backdrop { position: absolute; inset: 0; width: 100%; height: 100%; }

  .banner__photo {
    position: absolute; left: 359px; top: 52px; width: 162px; height: 384px;
    background: linear-gradient(180deg, var(--photo-light) 0%, var(--photo-dark) 45%, var(--photo-mid) 100%);
    border-radius: 60px 0 0 0;
  }

  .banner__button {
    position: absolute; left: 257px; top: 196px; width: 257px; height: 61px;
    border: 4px solid var(--button-rim); border-radius: 10px;
    background: linear-gradient(180deg, var(--button-top) 0%, var(--yellow-deep) 50%, var(--button-bottom) 100%);
    box-shadow: 0 4px 6px rgba(0,0,0,0.45);
    display: flex; align-items: center; justify-content: center;
    font-weight: 700; font-size: 30px; color: var(--text-dark);
  }

  .banner__brand {
    position: absolute; left: 150px; top: 380px;
    font-weight: 700; font-size: 27px; color: var(--brand); letter-spacing: -0.3px;
  }

  .service-list { position: absolute; left: 20px; top: 110px; list-style: none; }
  .service-list li {
    display: flex; align-items: center; height: 27px;
    font-size: 24px; color: var(--text-dark);
  }
  .service-list li::before {
    content: "➝"; color: var(--accent-red); font-size: 18px; width: 44px;
  }
  .service-list .service-list__goal { color: var(--accent-red); }

  .offer { position: absolute; font-weight: 700; color: var(--text-grey); line-height: 1; }
  .offer--portal { left: 30px; top: 117px; font-size: 27px; line-height: 33px; }
  .offer--tech { left: 14px; top: 206px; font-size: 22px; }
  .offer--tech strong { font-size: 30px; }
  .offer--software { left: 30px; top: 245px; font-size: 38px; }
  .offer--dev { left: 30px; top: 287px; font-size: 27px; }

  .frame-label {
    position: absolute; left: 0; width: 800px; text-align: center;
    font-size: 28px; color: var(--text-dark);
  }
  .frame-label--a { top: 530px; }
  .frame-label--b { top: 1111px; }
</style>
</head>
<body>
<div class="sheet">

  <section class="banner banner--a" aria-label="Frame A">
    <svg class="banner__backdrop" viewBox="0 0 298 249" preserveAspectRatio="none" aria-hidden="true">
      <defs>
        <linearGradient id="yellowWashA" x1="0" y1="0" x2="1" y2="0">
          <stop offset="0" stop-color="#f9d423"/>
          <stop offset="0.5" stop-color="#fff3a8"/>
          <stop offset="1" stop-color="#f9d423"/>
        </linearGradient>
      </defs>
      <path d="M0,0 H100 C120,40 150,52 222,56 L222,249 H0 Z" fill="url(#yellowWashA)"/>
      <path d="M60,249 C90,226 140,214 222,216 V249 Z" fill="#ffffff"/>
      <path d="M0,68 C40,52 75,58 115,60 C155,62 180,54 210,42 L210,192 C170,200 125,196 85,206 C52,214 22,226 0,236 Z" fill="#ffffff" stroke="#5e5e5e" stroke-width="3"/>
    </svg>
    <div class="banner__photo" role="img" aria-label="Photo of a thoughtful young professional sitting with a laptop"></div>
    <ul class="service-list">
      <li>Branding</li>
      <li>Planning</li>
      <li>Innovation</li>
      <li>Reserch</li>
      <li>Strategy</li>
      <li>Development</li>
      <li>Technology</li>
      <li class="service-list__goal">Success</li>
    </ul>
    <div class="banner__button">Click Here</div>
    <div class="banner__brand">bramtor-lune.net</div>
  </section>
  <p class="frame-label frame-label--a">Frame A</p>

  <section class="banner banner--b" aria-label="Frame B">
    <svg class="banner__backdrop" viewBox="0 0 298 249" preserveAspectRatio="none" aria-hidden="true">
      <defs>
        <linearGradient id="yellowWashB" x1="0" y1="0" x2="1" y2="0">
          <stop offset="0" stop-color="#f9d423"/>
          <stop offset="0.5" stop-color="#fff3a8"/>
          <stop offset="1" stop-color="#f9d423"/>
        </linearGradient>
      </defs>
      <path d="M0,0 H100 C120,40 150,52 222,56 L222,249 H0 Z" fill="url(#yellowWashB)"/>
      <path d="M60,249 C90,226 140,214 222,216 V249 Z" fill="#ffffff"/>
      <path d="M0,68 C40,52 75,58 115,60 C155,62 180,54 210,42 L210,192 C170,200 125,196 85,206 C52,214 22,226 0,236 Z" fill="#ffffff" stroke="#5e5e5e" stroke-width="3"/>
    </svg>
    <div class="banner__photo" role="img" aria-label="Photo of a thoughtful young professional sitting with a laptop"></div>
    <p class="offer offer--portal">Portalwise<br>Consulting</p>
    <p class="offer offer--tech"><strong>Corenet</strong> Technology</p>
    <p class="offer offer--software">Software</p>
    <p class="offer offer--dev">Development</p>
    <div class="banner__button">Click Here</div>
    <div class="banner__brand">bramtor-lune.net</div>
  </section>
  <p class="frame-label frame-label--b">Frame B</p>

</div>
</body>
</html>
```